Neues Flyer-Design gesucht
Zielgruppe
siehe Homepage www.lirok-bremen.de
Aufgabenstellung
Wir haben bereits einen Flyer und wünschen uns einen neuen, mit weniger Text und anderen Bildern. Wir sind auch offen für ein anderes Format.
In der Datei flyer_ueberarbeitung.docx haben wir andere Texte, sind jedoch nicht zufrieden damit und wünsche professionelle Hilfe :)

```html
<!DOCTYPE html>
<html lang="de">
<head>
<meta charset="utf-8">
<title>Lirok – Soziale Dienste · Flyer</title>
<link href="https://fonts.googleapis.com/css2?family=Fira+Sans:wght@400;500;600&display=swap" rel="stylesheet">
<style>
:root{
  --green:#86b425;
  --green-dark:#6f9d1a;
  --green-pale:#dbe7bf;
  --green-mist:#c9d6ad;
  --white:#ffffff;
  --ink:#4f4f4f;
  --bg:#eeeeee;
}
*{margin:0;padding:0;box-sizing:border-box}
html,body{width:1200px;height:675px;overflow:hidden;background:var(--bg);font-family:"Fira Sans",sans-serif}
.spread{position:absolute;top:152px;width:522px;height:370px;display:flex;background:var(--white);box-shadow:0 6px 18px rgba(0,0,0,.12)}
.spread--outside{left:66px}
.spread--inside{left:612px}
.panel{position:relative;width:50%;height:100%;display:flex;flex-direction:column;gap:3px;background:var(--white)}
.block{display:flex;flex-direction:column;align-items:center;justify-content:center;text-align:center;padding:0 14px}
.block--green{background:linear-gradient(180deg,var(--green-dark),var(--green));color:var(--white)}
.block--pale{background:linear-gradient(90deg,var(--green-pale),var(--green-mist));color:var(--ink)}
.block--white{background:var(--white);color:var(--ink)}
.photo{width:100%}
h2{font-weight:600;font-size:12.5px;letter-spacing:.2px;margin-bottom:5px;text-transform:uppercase}
h3{font-weight:600;font-size:6.2px;margin-top:5px}
p{font-size:6px;line-height:1.38;margin-bottom:5px}
p:last-child{margin-bottom:0}
.strong{font-weight:600}
.accent{color:var(--green);font-weight:600}
.contact p{margin-bottom:6px;font-size:5.8px}
.brand{display:flex;align-items:center;gap:8px;color:var(--green-dark);font-weight:500;font-size:15px}
.brand-dot{width:14px;height:14px;border-radius:50%;background:var(--green)}
.title{font-size:14px;font-weight:600;text-transform:uppercase;margin-bottom:4px}
.subtitle{font-size:7.5px;line-height:1.3;margin-bottom:10px}
.tagline{font-size:7px;font-weight:600;letter-spacing:.3px}
.heading-green{color:var(--green)}
</style>
</head>
<body>

<section class="spread spread--outside">
  <div class="panel">
    <div class="block block--green" style="height:160px">
      <h2>Was uns wichtig ist</h2>
      <p>Wir sehen es als unsere Aufgabe an, mit den KlientInnen partizipativ die eigenen Stärken zu aktivieren und sozialraumorientiert zu arbeiten, indem wir Netzwerke und Sozialräume mit den KlientInnen erschließen, die sie im Alltag unterstützen.</p>
      <p>Die besondere Bedeutung hinsichtlich Sensibilität, Wertschätzung, Offenheit, Toleranz und Transparenz im Umgang mit anderen Menschen kann nicht hoch genug eingeschätzt werden.</p>
      <p class="strong">Hedwig Albers hat dies folgendermaßen formuliert:<br>Keinen verderben lassen, auch nicht sich selber,<br>jeden mit Glück erfüllen, auch sich. Das ist gut.</p>
    </div>
    <div class="photo" role="img" aria-label="Foto: Familie als Silhouette im Sonnenuntergang, Hand in Hand" style="height:116px;background:linear-gradient(180deg,#c9a57a 0%,#e8b468 55%,#3a2a1e 100%)"></div>
    <div class="block block--pale contact" style="flex:1">
      <p class="strong">Lirok – Soziale Dienste</p>
      <p>Lindenweg 14 | 28195 Bremen-Mitte</p>
      <p>Tel: 0421/486 720 10 | Fax: 0421/486 720 19 | E-Mail: info@lirok-bremen.de</p>
      <p>Ansprechpartnerin: Frau Lena Marten</p>
      <p class="accent">www.lirok-bremen.de</p>
    </div>
  </div>
  <div class="panel">
    <div class="block block--pale" style="height:92px;background:linear-gradient(180deg,var(--green-pale),#e6eed2)">
      <div class="brand"><span class="brand-dot"></span><span>Lirok Soziale Dienste</span></div>
    </div>
    <div class="photo" role="img" aria-label="Foto: Eltern mit zwei Kindern kuscheln fröhlich auf dem Sofa" style="height:183px;background:linear-gradient(135deg,#d9d4cf,#a88e78 55%,#6b6d78)"></div>
    <div class="block block--green" style="flex:1">
      <div class="title">Hilfen zur Erziehung</div>
      <div class="subtitle">Sozialpädagogische Familienhilfe<br>Erziehungsbeistand</div>
      <div class="tagline">BETREUUNG | BEGLEITUNG | UNTERSTÜTZUNG</div>
    </div>
  </div>
</section>

<section class="spread spread--inside">
  <div class="panel">
    <div class="photo" role="img" aria-label="Foto: Mutter spricht mit einem Kind, das die Hände vors Gesicht hält" style="height:118px;background:linear-gradient(90deg,#e8d6c6,#6fae8e 45%,#b98a5c)"></div>
    <div class="block block--white" style="height:128px">
      <p>Wünschen Sie eine pädagogische Unterstützung für Ihre Familie?</p>
      <p>Sind Sie oder Ihre Familie durch Konflikte belastet,<br>die Sie am liebsten aus der Welt schaffen würden?</p>
      <p>Wünschen Sie sich eine Unterstützung in der Kooperation mit<br>Schulen und Kitas oder auch in Behördenangelegenheiten?</p>
      <p class="accent">Im Laufe eines Lebens können Situationen und Umstände entstehen, welche allein nur schwierig oder gar nicht bewältigt werden können. Gerne stehen wir Ihnen dabei zur Seite.</p>
    </div>
    <div class="block block--green" style="flex:1">
      <h2>Wer wir sind</h2>
      <p>Wir sind ein Team von pädagogischen Fachkräften,<br>welches vorrangig Erziehungsberatung leistet.</p>
      <p>Lirok – Soziale Dienste ist ein freier Träger der Kinder- und Jugendhilfe und arbeitet nach dem Kinder- und Jugendhilferecht des 8. Sozialgesetzbuches.</p>
      <p>Das heißt, wir bieten pädagogische Unterstützung im Rahmen<br>einer sogenannten „Hilfe zur Erziehung“ an.</p>
    </div>
  </div>
  <div class="panel">
    <div class="block block--green" style="height:176px">
      <h2>Was wir anbieten</h2>
      <h3>Sozialpädagogische Familienhilfe</h3>
      <p>Im Rahmen einer sozialpädagogischen Familienhilfe erfahren Familien direkt vor Ort eine pädagogische Unterstützung, vor allem in Form einer Erziehungsberatung.</p>
      <h3>Erziehungsbeistandschaft, auch für junge Volljährige</h3>
      <p>Mit einer Erziehungsbeistandschaft wird einem Kind oder Jugendlichen exklusiv eine pädagogische Fachkraft an die Seite gestellt. Ziel ist die Unterstützung des Kindes oder Jugendlichen in einer bestimmten Zeit.</p>
      <h3>Begleitete Umgänge</h3>
      <p>Nach einer Trennung der Eltern und/oder Gewaltvorwürfen kann es sinnvoll sein, dass die Kontakte zwischen einem Elternteil und Kind pädagogisch begleitet werden.</p>
    </div>
    <div class="photo" role="img" aria-label="Foto: Hände von Erwachsenen und Kindern übereinander gelegt" style="height:62px;background:linear-gradient(90deg,#cfc2b6,#e9a9a0 50%,#d8c9c0)"></div>
    <div class="block block--pale" style="flex:1">
      <h2 class="heading-green">Wie Sie Unterstützung erhalten</h2>
      <p>Sollten Sie eine pädagogische Unterstützung wünschen, ist der Allgemeine Soziale Dienst (ASD) des Jugendamtes Ihre erste Anlaufstelle. Mit Hilfe des Behördenfinders wissen Sie, welcher ASD für Sie zuständig ist:</p>
      <p class="accent">www.stadtportal-bremen.de/behoerdenfinder</p>
      <p>Im Gespräch mit dem ASD wird geprüft, ob ein pädagogischer Bedarf vorliegt. Falls dies zutrifft, wird mit Ihnen besprochen, welche Unterstützung für Sie am besten geeignet sein könnte.</p>
    </div>
  </div>
</section>

</body>
</html>
```